School Rules Posters

I would like a design for four different posters. Each one has a different purpose:

1: The Three Main rules

2: The Rewards

3: The Consequences

4: Consequences

At the moment they are very boring and dry and I would like an icon for each rule with the text underneath?

I'd like the logo on it.

It is for a middle school so it cannot be 'too young'.

I don't mind if the posters are Portrait or Landscape. The posters need to provide pupils with clarity and cannot be too busy. They'll be made into A1.
I have attached an example from another school which has logos - I don't want the same thing but give's you an idea of icons.

```html
<!DOCTYPE html>
<html lang="en">
<head>
<meta charset="utf-8">
<title>The Hartwell Way – Rules</title>
<link rel="stylesheet" href="https://fonts.googleapis.com/css2?family=Montserrat:wght@800&family=Oswald:wght@600;700&family=Rubik:wght@500;600&display=swap">
<style>
  :root {
    --blue-deep: #1b63a8;
    --blue-mid: #1a5fa8;
    --blue-light: #3a8fdd;
    --purple: #93307a;
    --ink: #111111;
    --paper: #ffffff;
    --mist: #f4f4f4;
    --rule: #e6e6e6;
  }
  * { box-sizing: border-box; margin: 0; padding: 0; }
  html, body { width: 1200px; height: 908px; overflow: hidden; background: var(--paper); }
  body { position: relative; font-family: "Rubik", Arial, sans-serif; }

  .masthead {
    position: absolute; left: 0; top: 0; width: 1200px; height: 142px;
    background: var(--blue-deep);
  }
  .masthead-rule {
    position: absolute; left: 0; top: 142px; width: 1200px; height: 6px;
    background: var(--purple);
  }
  .school-name {
    position: absolute; left: 26px; top: 30px; width: 130px;
    display: flex; flex-direction: column; align-items: center; gap: 10px;
    color: var(--paper); font-weight: 600; font-size: 16px; line-height: 1.15;
    text-align: center; letter-spacing: 0.5px;
  }
  .school-name .mark { width: 30px; height: 30px; background: var(--paper); }
  .title {
    position: absolute; left: 190px; right: 14px; top: 24px; text-align: center;
    font-family: "Montserrat", Arial, sans-serif; font-weight: 800;
    font-size: 52px; line-height: 1; color: var(--paper); letter-spacing: -0.5px;
    white-space: nowrap;
  }
  .subtitle {
    position: absolute; left: 190px; right: 14px; top: 92px; text-align: center;
    font-size: 27px; font-weight: 500; color: var(--paper); letter-spacing: 0.3px;
    line-height: 1.1; white-space: nowrap;
  }

  .band { position: absolute; left: 0; width: 1200px; display: grid;
    grid-template-columns: 242px 261px 208px 243px 246px; }
  .band-ready { top: 148px; height: 253px; }
  .band-respect { top: 406px; height: 236px; }
  .band-safe { top: 647px; height: 261px; }
  .band-line { position: absolute; left: 0; width: 1200px; height: 5px; }
  .line-respect { top: 401px; background: var(--blue-mid); }
  .line-safe { top: 642px; background: var(--blue-light); }

  .rule-cell {
    display: flex; flex-direction: column; align-items: center;
    text-align: center; font-size: 18px; font-weight: 600; line-height: 1.2;
  }
  .rule-cell + .rule-cell { border-left: 1px solid var(--rule); }
  .rule-cell svg { width: 64px; height: 64px; fill: none; stroke: currentColor;
    stroke-width: 3; stroke-linecap: round; stroke-linejoin: round; margin-bottom: 12px; }
  .band-ready .rule-cell { padding-top: 86px; color: var(--blue-mid); }
  .band-ready .rule-cell svg { color: var(--purple); }
  .band-respect .rule-cell { padding-top: 70px; color: var(--ink); font-weight: 500; }
  .band-respect .rule-cell svg { color: var(--blue-mid); }
  .band-respect .rule-cell:nth-child(odd) { background: var(--mist); }
  .band-respect .rule-cell + .rule-cell { border-left: none; }
  .band-safe .rule-cell { padding-top: 74px; color: var(--blue-mid); }
  .band-safe .rule-cell svg { color: var(--blue-light); }

  .section-tab {
    position: absolute; height: 58px; display: flex; align-items: center; justify-content: center;
    font-family: "Oswald", Impact, sans-serif; font-weight: 700; font-size: 46px;
    color: var(--paper); line-height: 1; letter-spacing: 0.5px; white-space: nowrap;
    clip-path: polygon(0 0, 100% 0, 94% 100%, 6% 100%);
  }
  .tab-ready { left: 447px; width: 306px; top: 148px; background: var(--purple); }
  .tab-respect { left: 405px; width: 390px; top: 406px; background: var(--blue-mid); }
  .tab-safe { left: 481px; width: 238px; top: 647px; background: var(--blue-light); }
</style>
</head>
<body>
  <header class="masthead">
    <div class="school-name"><span class="mark"></span>HARTWELL ACADEMY</div>
    <h1 class="title">THE HARTWELL WAY – RULES</h1>
    <p class="subtitle">HELPING US BE THE BEST WE CAN BE</p>
  </header>
  <div class="masthead-rule"></div>

  <section class="band band-ready">
    <div class="rule-cell">
      <svg viewBox="0 0 64 64"><path d="M4 22l10-8 6 8-10 8zM60 22l-10-8-6 8 10 8z"/><path d="M14 28l14 14c2 2 5 2 6 0M20 22l8-4h8l10 6M30 22l-6 6c-2 2 0 5 3 4l7-4 10 10M22 34l10 10M26 30l10 10"/></svg>
      Punctual to<br>Meet &amp; Great
    </div>
    <div class="rule-cell">
      <svg viewBox="0 0 64 64"><path d="M24 46c0-8-8-11-8-20a16 16 0 0 1 32 0c0 9-8 12-8 20z"/><path d="M25 51h14M26 56h12M29 61h6M32 2v5M12 10l3 3M52 10l-3 3M4 26h5M55 26h5"/></svg>
      Ready to learn new<br>ideas Ready to learn<br>new ideas
    </div>
    <div class="rule-cell">
      <svg viewBox="0 0 64 64"><rect x="6" y="28" width="10" height="28" rx="2"/><path d="M16 30l10-12 4-14c4 0 6 4 5 9l-3 9h20c4 0 5 5 2 7 3 1 3 6-1 7 3 2 2 6-2 7 2 2 0 6-4 6H22l-6-3"/></svg>
      Be Well<br>Presented
    </div>
    <div class="rule-cell">
      <svg viewBox="0 0 64 64"><path d="M50 34v22H8V14h34"/><path d="M18 32l10 10 28-30"/></svg>
      Have the right<br>equipment
    </div>
    <div class="rule-cell">
      <svg viewBox="0 0 64 64"><rect x="20" y="4" width="24" height="22" rx="4"/><path d="M28 10v8M36 10v8M32 26v28M14 34h36M22 30h20M20 54h24M20 54v6M44 54v6M32 54v6"/></svg>
      Know Your<br>Seat
    </div>
  </section>

  <div class="band-line line-respect"></div>
  <section class="band band-respect">
    <div class="rule-cell">
      <svg viewBox="0 0 64 64"><path d="M22 38V12a3 3 0 0 1 6 0v18M28 30V6a3 3 0 0 1 6 0v24M34 30V8a3 3 0 0 1 6 0v24M40 32V14a3 3 0 0 1 6 0v26c0 8-6 14-14 14h-4c-6 0-10-6-12-10l-4-8c-1-3 3-5 5-2l5 6"/><path d="M22 60h18"/></svg>
      Raise your hand<br>to talk
    </div>
    <div class="rule-cell">
      <svg viewBox="0 0 64 64"><path d="M32 58L8 34C0 26 2 12 14 10c8-1 14 4 18 10 4-6 10-11 18-10 12 2 14 16 6 24z"/><path d="M20 30l8-6h8l8 6M26 36l8 8M30 32l8 8M34 28l8 8"/></svg>
      Manners give a<br>great impressions
    </div>
    <div class="rule-cell">
      <svg viewBox="0 0 64 64"><rect x="16" y="4" width="32" height="56" rx="2"/><circle cx="40" cy="33" r="3"/></svg>
      Hold doors open<br>for others
    </div>
    <div class="rule-cell">
      <svg viewBox="0 0 64 64"><path d="M32 28l-9-9a6 6 0 0 1 9-8 6 6 0 0 1 9 8z"/><path d="M4 38h10v18H4zM14 40h12c4 0 6 4 2 6h-8M14 52l8 4h14l20-14c2-2 0-6-3-5l-13 7"/><path d="M14 12l4 3M50 12l-4 3M12 22h4M48 22h4"/></svg>
      Respect every persons<br>right to learn &amp; work
    </div>
    <div class="rule-cell">
      <svg viewBox="0 0 64 64"><circle cx="32" cy="24" r="18"/><path d="M32 14l3 7 7 1-5 5 1 7-6-3-6 3 1-7-5-5 7-1z"/><path d="M22 39v21l10-7 10 7V39"/></svg>
      Show the best<br>version of you
    </div>
  </section>

  <div class="band-line line-safe"></div>
  <section class="band band-safe">
    <div class="rule-cell">
      <svg viewBox="0 0 64 64"><path d="M14 6c6 0 8 8 6 16-1 4-8 4-9 0-2-8-2-16 3-16zM12 30h8v4c0 4-8 4-8 0zM46 24c6 0 6 8 4 16-1 4-8 4-9 0-2-8 0-16 5-16zM42 48h8v4c0 4-8 4-8 0z"/></svg>
      Walk quietly around<br>the school building<br>&amp; grounds
    </div>
    <div class="rule-cell">
      <svg viewBox="0 0 64 64"><path d="M8 30h24l-4 28H12z"/><path d="M14 36l6 12M24 36l-4 10"/><circle cx="44" cy="8" r="4"/><path d="M36 58V30c0-8 4-12 8-12s8 4 8 12v28M44 58V40M36 24l-8 6"/></svg>
      Throw litter in<br>the bin
    </div>
    <div class="rule-cell">
      <svg viewBox="0 0 64 64"><path d="M6 16h26l-4 44H10zM20 16l4-10 8-2"/><path d="M30 44c0-6 6-10 14-10s14 4 14 10zM30 48h28M30 52c0 4 4 6 14 6s14-2 14-6"/></svg>
      Eat and drink<br>in the designated<br>areas
    </div>
    <div class="rule-cell">
      <svg viewBox="0 0 64 64"><path d="M4 60V26h56v34M4 26v-4M10 18h12M10 14h8"/><path d="M50 16l-6 28M34 44h20M44 44v12M36 56h16"/></svg>
      Leave your desk tidy<br>for the next class
    </div>
    <div class="rule-cell">
      <svg viewBox="0 0 64 64"><path d="M4 58h56M8 58V22h18v36M26 58V14l26-6v50M14 4v18M12 30h3M19 30h3M12 38h3M19 38h3M12 46h3M19 46h3M32 22h4M42 20h4M32 32h4M42 30h4M32 42h4M42 40h4M36 58v-8h8v8"/></svg>
      Look after our<br>building and<br>grounds
    </div>
  </section>

  <div class="section-tab tab-ready">BE READY</div>
  <div class="section-tab tab-respect">BE RESPECTFUL</div>
  <div class="section-tab tab-safe">BE SAFE</div>
</body>
</html>
```